Serviceleitfaden für das Hotel
Zielgruppe
Lindholms Hotel
Hallo,
ich brauch eine Serviceleitfaden in Form eines Flyers
Titelseite:
Logo , darunter den Begriff : Serviceleitfaden
Innenseite 1 Links:
Fernsehprogramme
1. KMT
2. BWX
3. NPQ
4. Dux 1
5. Via Zehner
6. Welle Vier
7. Jul
8. Funk 7
9. NPQ 2
ab 10 die Programme von Orbo
http://business.orbo-tv.de/obs/cms/de/hotel-zimmerloesung-basispaket.jsp
alle Sender außer Orbo 3D
Innenseite 1 Rechts, Innenseite 2 Links und Rechts
Serviceleitfaden
http://www.hotel-lindholms.de/de/zimmer/service-leitfaden
Rückseite:
Telefonnummern
Internet
Sie könne sich kostenlos bei Netzwerkfunkhaus über Wlan anmelden.
Danach müssen Sie nur Ihren Browser öffnen.
Anfahrskizze:
Siehe Bild
Druckformat:
http://www.papierwerk-online.de/tpl/holt-team/media/pdv/druckdatenskizzen/faltblatt__gefalzt_auf_din_a4__6-seiter_%28zickzackfalz%29_2.pdf
http://www.papierwerk-online.de/tpl/holt-team/media/pdv/druckdatenskizzen/faltblatt__gefalzt_auf_din_a4__6-seiter_%28zickzackfalz%29_1.pdf

```html
<!DOCTYPE html>
<html lang="de">
<head>
<meta charset="utf-8">
<title>Lindholms Hotel – Serviceleitfaden Innenseite</title>
<link href="https://fonts.googleapis.com/css2?family=Arimo:wght@400;700&display=swap" rel="stylesheet">
<style>
  :root{
    --gold:#9a7d43;
    --ink:#1d1d1b;
    --paper:#ffffff;
    --backdrop:#ffffff;
    --grey:#8a8a8a;
  }
  *{margin:0;padding:0;box-sizing:border-box}
  html,body{width:1200px;height:848px;overflow:hidden;background:var(--backdrop)}
  body{position:relative;font-family:"Arimo",Arial,sans-serif;color:var(--ink)}
  .sheet{position:absolute;left:68px;top:161px;width:1067px;height:503px;background:var(--paper)}
  .band{position:absolute;left:0;top:0;width:100%;height:101px;background:var(--gold)}
  .panel-title{position:absolute;top:76px;color:#fff;font-size:12.5px;font-weight:400;letter-spacing:.3px}
  .abs{position:absolute}
  .channel-list{list-style:none;left:46px;top:121px;font-size:6.4px;font-weight:700}
  .channel-list li{height:18px;line-height:9px}
  .channel-list .num{display:inline-block;width:13px;color:var(--gold);font-weight:400}
  .column{width:114px;font-size:6.6px;line-height:9px;hyphens:auto}
  .column h3{color:var(--gold);font-size:6.6px;font-weight:400;text-transform:uppercase}
  .column p{margin-bottom:9px}
  .column ul{list-style:none;margin-bottom:9px}
  .bullets li{padding-left:4px;text-indent:-4px}
  .pkg-label{left:46px;top:336px;font-size:6.4px;font-weight:700}
  .pkg-name{left:46px;top:362px;font-size:13px;color:var(--grey);font-weight:400}
  .pkg-note{left:46px;top:391px;font-size:6.3px}
  .welcome{left:779px;top:225px;width:220px;text-align:center;font-size:8.3px;line-height:10.8px}
  .welcome h2{color:var(--gold);font-size:8.4px;font-weight:400;letter-spacing:.3px;margin-bottom:10px}
  .welcome p{margin-bottom:10.8px}
  .welcome .sign{color:var(--gold);font-size:8.4px;letter-spacing:.3px}
  .brand{white-space:nowrap}
  .brand-main{left:816px;top:40px;width:140px;text-align:center;color:#fff;font-size:19px;line-height:24px;font-weight:400}
  .footer-rule{position:absolute;left:0;top:459px;width:100%;height:1px;background:var(--gold)}
  .brand-foot{top:453px;background:var(--paper);padding:0 8px;color:var(--gold);font-size:9px;line-height:12px}
</style>
</head>
<body>
<div class="sheet">
  <div class="band"></div>
  <h1 class="panel-title" style="left:101px">FERNSEHPROGRAMME</h1>
  <h1 class="panel-title" style="left:456px">FERNSEHPROGRAMME</h1>

  <div class="abs brand brand-main">Lindholms Hotel</div>

  <ol class="abs channel-list">
    <li><span class="num">1</span>KMT</li>
    <li><span class="num">2</span>BWX</li>
    <li><span class="num">3</span>NPQ</li>
    <li><span class="num">4</span>DUX 1</li>
    <li><span class="num">5</span>VIA ZEHNER</li>
    <li><span class="num">6</span>WELLE VIER</li>
    <li><span class="num">7</span>JUL</li>
    <li><span class="num">8</span>FUNK 7</li>
    <li><span class="num">9</span>NPQ 2</li>
  </ol>
  <div class="abs pkg-label">AB 10 DIE PROGRAMME VON</div>
  <div class="abs pkg-name">Orbo Business</div>
  <div class="abs pkg-note">Alle Sender bis auf Orbo 3D</div>

  <div class="abs column" style="left:197px;top:123px">
    <h3>Orbo Cinema HD</h3>
    <p>Das Privatkino in Ihrem Hotelzimmer mit rund 20 deutschen TV-Premieren. Ob Komödie, Romanze, Science-Fiction oder Thriller.</p>
    <h3>Orbo Action HD</h3>
    <p>Hochspannung garantiert:<br>24 Stunden am Tag Adrenalin pur mit Action, Horror und Science-Fiction.</p>
    <h3>Orbo Hits HD</h3>
    <p>Die größten Kinohits der letzten Jahrzehnte mit allen technischen Vorteilen.</p>
    <h3>Orbo Atlantic HD</h3>
    <p>Die besten Produktionen von NGS, dem erfolgreichsten US-Premium-Sender, ausgewählte NGS-Filmhighlights und NGS-Dokumentationen. Alle Serien werden sowohl in Deutsch als auch in englischer Originalfassung verfügbar sein.</p>
    <h3>Orbo Sport News HD</h3>
    <p>Mit Orbo Sport News bleiben Sie im weltweiten Sportgeschehen immer auf dem Laufenden. Der einzige Sender in Deutschland und Österreich, der täglich 24 Stunden Sportnachrichten live präsentiert.</p>
  </div>

  <div class="abs column" style="left:401px;top:123px">
    <h3>Orbo Sport HD1 + HD2</h3>
    <ul class="bullets">
      <li>· Kontinental-Meisterliga: live</li>
      <li>· Landespokal: live</li>
      <li>· Kontinental-Pokalliga: live</li>
      <li>· Insel-Liga: live</li>
      <li>· Golf: Atlantic Golf Tour und Euro Links Tour sowie alle vier Major-Turniere und der Harbor Cup</li>
      <li>· Tennis aus Ashbury</li>
      <li>· Die Formel Prime</li>
    </ul>
    <h3>Orbo Sport Austria</h3>
    <p>Auf Orbo Sport Austria sind alle Spiele der Alpenliga und der Orbo Erste Liga für Sie erhältlich. Top-Klubs wie FC Salzachtal, SV Donaustadt oder Wiener Athletik live, das Live-Magazin „Tor und Takt“ und Top-Begegnungen der Alpen Basketball Liga – alles live.</p>
    <h3>Orbo Oberliga HD1 + HD2</h3>
    <p>Der Klassiker für echte Fußballfans: Die Fußball Oberliga und 2. Oberliga live und in HD sowie Konferenzschaltung bei Parallelspielen der Oberliga und 2. Oberliga</p>
    <h3>Meridian Channel HD</h3>
    <p>Exklusiven Serien als deutsche TV-Premieren und mitreißenden Blockbustern.</p>
  </div>

  <div class="abs column" style="left:552px;top:123px">
    <h3>Terra Explorer<br>Channel HD</h3>
    <p>Für echte Entdecker mit faszinierenden Bildern, packenden Geschichten und informativen Dokumentationen, von den entlegensten Winkeln der Welt bis zu den Zentren der Moderne.</p>
    <h3>Terra Wild HD</h3>
    <p>Faszinierende Natur und Tierwelt. Von fernen Naturparadiesen dieser Erde und den Tiefen der Ozeane bis hin zu Europas Naturparks.</p>
    <h3>Vixen HD</h3>
    <p>Preisgekrönte Top-Serien als deutsche TV-Erstausstrahlung sowie Thriller-, Kult- und Comedyserien,</p>
    <h3>Lantern Channel HD</h3>
    <p>Lantern-Kinoklassikern und die neuesten Lantern- und Pixelmoon-Filmhighlights. Perfekte TV-Unterhaltung für die ganze Familie.</p>
    <h3>Goldlion Channel HD</h3>
    <p>Besten Filmhighlights aus der Traumfabrik Hollywood in brillantem HD, unvergessliche Klassiker, beliebte Blockbuster, erfolgreiche Filmreihen und preisgekrönte Lieblingsstreifen.</p>
  </div>

  <div class="abs welcome">
    <h2>LIEBE GÄSTE UND FREUNDE VOM<br>LINDHOLMS HOTEL GARNI IN BRAKENDORF</h2>
    <p>In diesem Serviceleitfaden<br>finden Sie eine Auflistung und wichtige<br>Informationen von unseren Hotelleistungen.</p>
    <p>Sollten Sie weitere Wünsche haben,<br>so sprechen Sie uns bitte darauf an.<br>Wir sind gerne für Sie da.</p>
    <p>Wir wünschen Ihnen einen angenehmen<br>Aufenthalt in unserem Haus!</p>
    <div class="sign">IHR TEAM VOM LINDHOLMS HOTEL</div>
  </div>

  <div class="footer-rule"></div>
  <div class="abs brand brand-foot" style="left:135px">Lindholms Hotel</div>
  <div class="abs brand brand-foot" style="left:490px">Lindholms Hotel</div>
</div>
</body>
</html>
```